Brindle Capital and Investments

Create a simple business card design using the logos attached. Make it similar but not exact to the reference photo. Brand guidelines are also included.

```html
<!DOCTYPE html>
<html lang="en">
<head>
<meta charset="utf-8">
<title>Brindle Capital – Business Card</title>
<link href="https://fonts.googleapis.com/css2?family=Lato:wght@400;700;900&display=swap" rel="stylesheet">
<style>
  :root {
    --navy: #0b1442;
    --rust: #a4531c;
    --ink: #1c1c1c;
    --paper: #ffffff;
    --backdrop: #1b1b1d;
    --rule: #3a3a3a;
  }
  * { margin: 0; padding: 0; box-sizing: border-box; }
  html, body { width: 1200px; height: 1200px; overflow: hidden; }
  body {
    background: var(--backdrop);
    font-family: "Lato", sans-serif;
    position: relative;
  }
  .card {
    position: absolute;
    left: 160px;
    width: 880px;
    height: 500px;
    overflow: hidden;
  }
  .card-back { top: 70px; background: var(--navy); }
  .card-front { top: 630px; background: var(--paper); }

  .wordmark {
    display: flex;
    align-items: center;
    gap: 18px;
    font-family: "Lato", sans-serif;
    font-weight: 900;
    text-transform: uppercase;
    letter-spacing: 0.14em;
    line-height: 1;
  }
  .wordmark-dot {
    width: 22px; height: 22px;
    border-radius: 50%;
    background: var(--rust);
    flex: none;
  }
  .card-back .wordmark {
    position: absolute;
    left: 0; right: 0; top: 0; bottom: 0;
    justify-content: center;
    color: var(--paper);
    font-size: 52px;
  }
  .card-front .wordmark {
    position: absolute;
    right: 50px; top: 120px;
    color: var(--navy);
    font-size: 30px;
    gap: 12px;
  }
  .card-front .wordmark-dot { width: 16px; height: 16px; }

  .holder { position: absolute; left: 50px; top: 190px; }
  .holder-name {
    font-weight: 900;
    font-size: 38px;
    color: var(--navy);
    text-transform: uppercase;
    letter-spacing: -0.01em;
  }
  .holder-title { font-size: 24px; color: var(--ink); margin-top: 2px; }

  .divider {
    position: absolute;
    left: 40px; right: 40px; top: 290px;
    height: 2px; background: var(--rule);
  }

  .contact-list { position: absolute; left: 50px; top: 318px; list-style: none; }
  .contact-item {
    display: flex; align-items: center; gap: 18px;
    font-size: 25px; color: var(--ink);
    margin-bottom: 10px;
  }
  .contact-icon { width: 30px; height: 26px; flex: none; }

  .address {
    position: absolute;
    right: 50px; top: 318px;
    text-align: right;
    font-size: 25px; color: var(--ink);
    line-height: 1.4;
  }

  .footer-bands { position: absolute; left: 0; bottom: 0; width: 880px; height: 90px; }
  .website {
    position: absolute;
    right: 50px; bottom: 14px;
    font-size: 24px; color: var(--paper);
    letter-spacing: 0.02em;
  }
</style>
</head>
<body>

<section class="card card-back" aria-label="Card back">
  <div class="wordmark"><span class="wordmark-dot"></span>Brindle Capital</div>
</section>

<section class="card card-front" aria-label="Card front">
  <div class="wordmark"><span class="wordmark-dot"></span>Brindle Capital</div>

  <div class="holder">
    <h1 class="holder-name">Daniel Carter</h1>
    <p class="holder-title">Managing Director</p>
  </div>

  <div class="divider"></div>

  <ul class="contact-list">
    <li class="contact-item">
      <svg class="contact-icon" viewBox="0 0 24 24" aria-hidden="true">
        <path fill="var(--rust)" d="M6.6 10.8c1.4 2.8 3.8 5.1 6.6 6.6l2.2-2.2c.3-.3.7-.4 1-.2 1.1.4 2.3.6 3.6.6.6 0 1 .4 1 1V20c0 .6-.4 1-1 1C10.6 21 3 13.4 3 4c0-.6.4-1 1-1h3.5c.6 0 1 .4 1 1 0 1.3.2 2.5.6 3.6.1.3 0 .7-.2 1z"/>
      </svg>
      044-987 654 321
    </li>
    <li class="contact-item">
      <svg class="contact-icon" viewBox="0 0 24 20" aria-hidden="true">
        <path fill="var(--rust)" d="M1 2h22v16H1z"/>
        <path fill="none" stroke="var(--paper)" stroke-width="1.8" d="M1 2l11 9 11-9"/>
      </svg>
      hello@brindlecap.com
    </li>
  </ul>

  <address class="address" style="font-style:normal">
    87, Harrow Lane, Suite 4<br>
    45452, Country name
  </address>

  <svg class="footer-bands" viewBox="0 0 880 90" aria-hidden="true">
    <polygon points="0,22 520,22 506,38 0,38" fill="var(--rust)"/>
    <polygon points="0,44 500,44 540,10 880,10 880,90 0,90" fill="var(--navy)"/>
    <polygon points="0,56 0,90 880,90 880,90" fill="var(--navy)"/>
  </svg>
  <div class="website">www.brindlecap.com</div>
</section>

</body>
</html>
```